Flyer Design Project

I give out flyers at bridal shows. Couples hire me to photograph guests upon arrival and have pictures printed to bring home as a wedding favor before the party is over

Target Market(s)

Female brides 20-30 years old, middle class, New Jersey USA, sentimental, feminine

Industry/Entity Type

Wedding

Font styles to use
Sans Serif

Colors

Designer to choose colors to be used in the design.

Requirements
Must have
• Feminine touches without being too much, easy on the eye (not too busy). Please have nice border/graphics around the main photo on the front page. Ok to crop photo. Ok to have photo(s) all the way to the page edge (or not - you know best)
Should not have
• Do not use my rough draft as it is. I simply provided it to show the key parts and order they should appear in.

```html
<!DOCTYPE html>
<html lang="en">
<head>
<meta charset="utf-8">
<title>SnapKeepsake – Bridal Show Flyer</title>
<link rel="stylesheet" href="https://fonts.googleapis.com/css2?family=Montserrat:wght@600;700;800;900&family=Raleway:wght@400;600&display=swap">
<style>
  :root {
    --stage: #6d6e71;
    --paper: #ffffff;
    --navy: #2f3f8f;
    --red: #b4232a;
    --orange-deep: #f26a21;
    --ink: #2b2e33;
    --text: #3a3d42;
    --gold: #f5a623;
  }
  * { margin: 0; padding: 0; box-sizing: border-box; }
  html, body { width: 1200px; height: 1000px; overflow: hidden; }
  body { background: var(--stage); position: relative; font-family: "Raleway", sans-serif; }

  .flyer {
    position: absolute; left: 246px; top: 42px; width: 708px; height: 916px;
    background: var(--paper); overflow: hidden;
    box-shadow: 0 2px 8px rgba(0,0,0,.25);
  }
  .floral-backdrop {
    position: absolute; inset: 0;
    background: radial-gradient(ellipse at 20% 70%, #eef0f2 0%, #f7f8f9 40%, #ffffff 75%),
                linear-gradient(180deg, #f4f5f6, #ffffff);
  }
  .hero-art { position: absolute; left: 0; top: 0; width: 708px; height: 560px; }

  .brand {
    position: absolute; left: 30px; top: 56px; display: flex; align-items: center; gap: 8px;
    font-family: "Montserrat", sans-serif; font-weight: 800; font-size: 28px; color: var(--navy);
    letter-spacing: -0.5px;
  }
  .brand-dot { width: 14px; height: 14px; border-radius: 50%; background: var(--red); }

  .headline { position: absolute; right: 28px; top: 508px; text-align: right; font-family: "Montserrat", sans-serif; font-weight: 900; line-height: 1; }
  .headline .line-1 { font-size: 62px; color: var(--navy); letter-spacing: 0; }
  .headline .line-2 { font-size: 100px; letter-spacing: 1px; margin-top: -10px; }
  .headline .the {
    background: linear-gradient(180deg, var(--gold), var(--orange-deep));
    -webkit-background-clip: text; background-clip: text; color: transparent;
  }
  .headline .love { color: var(--red); }
  .tagline {
    position: absolute; left: 158px; top: 656px;
    font-family: "Montserrat", sans-serif; font-weight: 800; font-size: 21px; color: var(--ink); letter-spacing: 1px;
  }

  .benefits { position: absolute; left: 0; top: 700px; width: 708px; height: 156px; display: flex; }
  .benefit { padding: 12px 14px 0 22px; font-size: 12.5px; line-height: 1.3; color: var(--text); }
  .benefit:nth-child(1) { width: 246px; }
  .benefit:nth-child(2) { width: 228px; border-left: 2px solid var(--ink); border-right: 2px solid var(--ink); padding-left: 28px; padding-right: 22px; }
  .benefit:nth-child(3) { width: 234px; padding-right: 40px; }
  .benefit .em-navy, .benefit .em-red {
    font-family: "Montserrat", sans-serif; font-weight: 800; display: block; line-height: 1.05;
  }
  .em-navy { color: var(--navy); font-size: 16px; margin-top: 2px; }
  .em-red { color: var(--red); font-size: 18px; }
  .benefit b { font-weight: 700; color: var(--ink); }

  .contact-bar {
    position: absolute; left: 0; bottom: 0; width: 708px; height: 60px; background: var(--ink);
    font-family: "Montserrat", sans-serif; color: #fff;
  }
  .contact-bar .web, .contact-bar .mail {
    position: absolute; top: 27px; font-size: 9.5px; font-weight: 600; letter-spacing: 1.6px; white-space: nowrap;
  }
  .contact-bar .web { left: 46px; }
  .contact-bar .mail { left: 283px; }
  .contact-bar .call { position: absolute; right: 18px; top: 7px; text-align: center; }
  .call .label { font-size: 8.5px; letter-spacing: 1.5px; font-weight: 600; }
  .call .number { font-size: 28px; font-weight: 800; color: var(--gold); letter-spacing: 1px; line-height: 1.1; }
</style>
</head>
<body>
  <main class="flyer">
    <div class="floral-backdrop" role="img" aria-label="Soft white flower petals background"></div>

    <svg class="hero-art" viewBox="0 0 708 560" xmlns="http://www.w3.org/2000/svg">
      <defs>
        <linearGradient id="photoTone" x1="0" y1="0" x2="1" y2="1">
          <stop offset="0" stop-color="#e9e6e1"/>
          <stop offset="0.45" stop-color="#c99a7f"/>
          <stop offset="0.75" stop-color="#5a5457"/>
          <stop offset="1" stop-color="#3c3a3d"/>
        </linearGradient>
        <linearGradient id="navyRibbon" x1="0" y1="0" x2="1" y2="0">
          <stop offset="0" stop-color="#34449a"/>
          <stop offset="0.6" stop-color="#1f2b5e"/>
          <stop offset="1" stop-color="#151a33"/>
        </linearGradient>
        <linearGradient id="redRibbon" x1="0" y1="0" x2="1" y2="0">
          <stop offset="0" stop-color="#7a1418"/>
          <stop offset="1" stop-color="#e3262d"/>
        </linearGradient>
      </defs>
      <path role="img" aria-label="Photo of four smiling bridesmaids in dark strapless gowns at a wedding reception"
            fill="url(#photoTone)"
            d="M0 0 H708 V345 C600 360 480 400 360 440 C240 475 120 470 0 420 Z"/>
      <path fill="url(#navyRibbon)"
            d="M0 420 C120 470 240 475 360 440 C300 480 240 510 160 520 C100 525 40 515 0 500 Z"/>
      <path fill="url(#redRibbon)"
            d="M708 345 C600 360 480 400 360 440 C260 475 210 500 180 515 C300 505 420 470 520 440 C590 420 650 410 708 410 Z"/>
    </svg>

    <div class="brand"><span class="brand-dot"></span>SnapKeepsake</div>

    <h1 class="headline">
      <div class="line-1">SPREADING</div>
      <div class="line-2"><span class="the">THE </span><span class="love">LOVE</span></div>
    </h1>
    <p class="tagline">ONE PHOTO AT A TIME!</p>

    <section class="benefits">
      <div class="benefit">
        You're marrying the love of your life, the one who makes you feel special.
        <span class="em-navy">NOW SHARE THAT</span>
        <span class="em-red">LOVE</span>
        with your family and friends, and make them feel special, too!
      </div>
      <div class="benefit">
        <span class="em-navy">SURPRISE YOUR GUESTS WITH</span>
        <span class="em-red">THEIR OWN PHOTO FAVOR,</span>
        taken as they arrive to your reception and ready to bring home <b>before</b> the celebration is even over!
      </div>
      <div class="benefit">
        Everybody loves a good looking picture of themselves.
        <span class="em-navy">SO GIVE THEM AN</span>
        <span class="em-red">AWARD WINNING FAVOR</span>
        that will last forever as a happy memory of your day!
      </div>
    </section>

    <footer class="contact-bar">
      <span class="web">WWW.SNAPKEEP4U.COM</span>
      <span class="mail">INFO@SNAPKEEP4U.COM</span>
      <div class="call">
        <div class="label">CALL / TEXT:</div>
        <div class="number">555-013-2478</div>
      </div>
    </footer>
  </main>
</body>
</html>
```